International Trading Company, 'ZAVRO' needs a Business Card

The company name is "ZAVRO" and it has own logo design.
I'd like to use its logo on this business card.
I need two side Business Card.
I'll look forward to your great design.
Thank you very much in advance.

Contact Information for Business Card

Company Name : Zavro Harbour Limited
Information Example
Dorian Pallister
Mobile(use icon please) : 1 (212) 555-0143
Tel(use icon please) : 1 (212) 555-0178
Email(use icon please) : dorian27@zavroharbour-mail.com
Address(use icon please) : 482 Halden Ave, New York, NY 10160, USA

```html
<!DOCTYPE html>
<html lang="en">
<head>
<meta charset="utf-8">
<title>Zavro Harbour Limited – Business Card</title>
<link rel="stylesheet" href="https://fonts.googleapis.com/css2?family=Lato:wght@400;700;900&display=swap">
<style>
  :root {
    --stage: #2b2b2b;
    --card: #151515;
    --card-edge: #1f1f1f;
    --ink: #ffffff;
    --ink-soft: #e6e6e6;
    --front-mark: #cfcfcf;
    --rule: #8a8a8a;
  }
  * { box-sizing: border-box; margin: 0; padding: 0; }
  html, body {
    width: 1200px; height: 1189px; overflow: hidden;
    background: var(--stage);
    font-family: "Lato", Arial, sans-serif;
    color: var(--ink);
  }
  .sheet {
    width: 1200px; height: 1189px;
    display: flex; flex-direction: column; align-items: center; justify-content: center;
    gap: 64px;
  }
  .card {
    position: relative;
    width: 760px; height: 434px;
    background: var(--card);
    border: 1px solid var(--card-edge);
    border-radius: 28px;
    box-shadow: 0 18px 40px rgba(0,0,0,0.45);
    overflow: hidden;
  }
  .card-front { display: flex; align-items: center; justify-content: center; }
  .brand-name {
    font-weight: 900; letter-spacing: 3px; line-height: 1; white-space: nowrap;
  }
  .card-front .brand-name { font-size: 104px; color: var(--front-mark); }
  .card-back .brand-name {
    position: absolute; left: 64px; top: 196px;
    font-size: 80px; color: var(--ink);
  }
  .divider {
    position: absolute; left: 382px; top: 100px;
    width: 1px; height: 176px; background: var(--rule);
  }
  .contact {
    position: absolute; left: 412px; top: 96px;
  }
  .person-name { font-weight: 700; font-size: 24px; margin-bottom: 16px; }
  .contact-list { list-style: none; }
  .contact-item {
    display: flex; align-items: center; gap: 12px;
    font-size: 17px; color: var(--ink-soft); line-height: 1; margin-bottom: 12px;
    white-space: nowrap;
  }
  .contact-item svg { width: 16px; height: 16px; flex: none; }
  .address {
    position: absolute; left: 0; right: 0; bottom: 62px;
    text-align: center; font-size: 24px; color: var(--ink-soft);
  }
</style>
</head>
<body>
<main class="sheet">
  <section class="card card-front" aria-label="Business card front">
    <span class="brand-name">ZAVRO</span>
  </section>

  <section class="card card-back" aria-label="Business card back">
    <span class="brand-name">ZAVRO</span>
    <div class="divider"></div>
    <div class="contact">
      <p class="person-name">Dorian Pallister</p>
      <ul class="contact-list">
        <li class="contact-item">
          <svg viewBox="0 0 16 16" aria-hidden="true"><rect x="3.5" y="1" width="9" height="14" rx="1.5" fill="none" stroke="#fff" stroke-width="1.4"/><circle cx="8" cy="12.5" r="0.9" fill="#fff"/></svg>
          <span>1 (212) 555-0143</span>
        </li>
        <li class="contact-item">
          <svg viewBox="0 0 16 16" aria-hidden="true"><path d="M1 6c0-2 3-3.5 7-3.5S15 4 15 6v1.2h-3.4V5.6H4.4v1.6H1z" fill="#fff"/><path d="M3 8.5h10l1 5.5H2z" fill="#fff"/><circle cx="8" cy="11" r="1.4" fill="#151515"/></svg>
          <span>1 (212) 555-0178</span>
        </li>
        <li class="contact-item">
          <svg viewBox="0 0 16 16" aria-hidden="true"><rect x="1" y="3" width="14" height="10" fill="#fff"/><path d="M1.5 3.5 8 9l6.5-5.5M1.5 12.5 6 8M14.5 12.5 10 8" fill="none" stroke="#151515" stroke-width="1.1"/></svg>
          <span>dorian27@zavroharbour-mail.com</span>
        </li>
      </ul>
    </div>
    <p class="address">482 Halden Ave, New York, NY 10160, USA</p>
  </section>
</main>
</body>
</html>
```